Family owned plumbing contractor needs eye catching business card design

Business cards that are unique, eye catching, and provide customers with general company information, such as name, address, phone number, website, employee name/title, cell phone #, & email address. We are transitioning to a new logo that utilizes a more retro feel, so we are interested in seeing some cool old school designs in the mix. We are liking the dark background on some of the samples on this website. If that is workable with our artwork, we would like to see that incorporated into the design.
Contact Information for Business Card
Copperline Pipeworks, Inc.
www.copperlinepipeworks.example
(555) 392-7068 phone
Nevada License #64205
California License #5810473
Dale Wrennick, President
(555) 618-9032 cell
dale@copperlinepipeworks.example
Residential * Commercial * Service
Requirements
Must have
- The business card details listed above & logo provided.
Nice to have
- I made some notes about color options in the description.

```html
<!DOCTYPE html>
<html lang="en">
<head>
<meta charset="utf-8">
<title>Copperline Pipeworks, Inc. — Business Card</title>
<link rel="stylesheet" href="https://fonts.googleapis.com/css2?family=Tinos:ital,wght@0,400;0,700;1,400;1,700&display=swap">
<style>
  :root {
    --page: #2b2b2d;
    --slate: #4e6f8c;
    --slate-soft: #5a7b97;
    --paper: #ffffff;
    --paper-vein: #f1f3f6;
    --ink: #1c1c1c;
    --brand-blue: #4b6a88;
    --mint: #6cc3a8;
    --white: #ffffff;
  }
  * { box-sizing: border-box; margin: 0; padding: 0; }
  html, body { width: 1200px; height: 905px; overflow: hidden; }
  body {
    background: var(--page);
    font-family: "Tinos", "Times New Roman", serif;
    position: relative;
  }
  .card {
    position: absolute;
    width: 620px;
    height: 354px;
    border-radius: 4px;
    box-shadow: 0 10px 28px rgba(0,0,0,.45);
    overflow: hidden;
  }
  .card-texture { position: absolute; inset: 0; }

  /* Front */
  .card-front { left: 150px; top: 70px; background: var(--slate); }
  .card-front .card-texture {
    background: radial-gradient(ellipse at 30% 40%, var(--slate-soft), var(--slate) 70%);
  }
  .front-mark {
    position: absolute;
    left: 0; right: 0; top: 110px;
    display: flex; align-items: center; justify-content: center; gap: 16px;
  }
  .brand-dot {
    width: 30px; height: 30px; border-radius: 50%;
    background: var(--mint);
  }
  .front-mark .brand-name {
    color: var(--white);
    font-weight: 700;
    font-size: 38px;
    letter-spacing: .5px;
  }
  .tagline {
    position: absolute;
    left: 0; right: 0; top: 235px;
    text-align: center;
    color: var(--white);
    font-size: 22px;
    font-style: italic;
    letter-spacing: 1px;
  }
  .tagline .sep { margin: 0 12px; }

  /* Back */
  .card-back { left: 430px; top: 480px; background: var(--paper); }
  .card-back .card-texture {
    background: radial-gradient(ellipse at 70% 60%, var(--paper-vein), var(--paper) 75%);
  }
  .back-mark {
    position: absolute;
    right: 34px; top: 64px;
    width: 260px;
    display: flex; align-items: center; gap: 12px;
  }
  .back-mark .brand-dot { width: 22px; height: 22px; flex: none; }
  .back-mark .brand-name {
    color: var(--brand-blue);
    font-weight: 700;
    font-size: 25px;
    line-height: 1.15;
  }
  .holder { position: absolute; left: 34px; top: 44px; }
  .holder-name {
    color: var(--brand-blue);
    font-weight: 700;
    font-size: 28px;
    letter-spacing: 1px;
    text-transform: uppercase;
  }
  .holder-title {
    color: var(--brand-blue);
    font-weight: 700;
    font-size: 15px;
    letter-spacing: 1.5px;
    text-transform: uppercase;
    margin-top: 2px;
  }
  .licenses { margin-top: 8px; color: var(--ink); font-size: 16px; line-height: 1.25; }
  .contact-row {
    position: absolute; left: 40px;
    display: flex; align-items: center; gap: 12px;
    color: var(--ink); font-size: 17px; line-height: 1.3;
  }
  .contact-row.phones { top: 210px; }
  .contact-row.online { top: 280px; }
  .contact-icon { width: 34px; height: 34px; flex: none; }
  .contact-rule { width: 2px; height: 44px; background: var(--brand-blue); flex: none; }
</style>
</head>
<body>

  <section class="card card-front" aria-label="Card front">
    <div class="card-texture" role="img" aria-label="Soft slate-blue marble texture"></div>
    <div class="front-mark">
      <span class="brand-dot"></span>
      <span class="brand-name">Copperline Pipeworks, Inc.</span>
    </div>
    <p class="tagline">Residential<span class="sep">•</span>Commercial<span class="sep">•</span>Service</p>
  </section>

  <section class="card card-back" aria-label="Card back">
    <div class="card-texture" role="img" aria-label="Faint white marble texture"></div>

    <div class="holder">
      <h1 class="holder-name">Dale Wrennick</h1>
      <p class="holder-title">President</p>
      <p class="licenses">Nevada License #64205<br>California License #5810473</p>
    </div>

    <div class="back-mark">
      <span class="brand-dot"></span>
      <span class="brand-name">Copperline Pipeworks, Inc.</span>
    </div>

    <div class="contact-row phones">
      <svg class="contact-icon" viewBox="0 0 34 34" aria-hidden="true">
        <circle cx="17" cy="17" r="15" fill="none" stroke="var(--brand-blue)" stroke-width="2"/>
        <path d="M12 11c1-1 2-1 3 0l1 2c.5 1 0 1.6-.6 2.2.8 1.6 2 2.8 3.4 3.6.6-.6 1.2-1.1 2.2-.6l2 1c1 1 1 2 0 3-2 2-5 1-8-2s-5-7-3-9.2z" fill="var(--brand-blue)"/>
      </svg>
      <span class="contact-rule"></span>
      <p>Office : (555) 392-7068<br>Cell : (555) 618-9032</p>
    </div>

    <div class="contact-row online">
      <svg class="contact-icon" viewBox="0 0 34 34" aria-hidden="true">
        <circle cx="17" cy="17" r="15" fill="none" stroke="var(--brand-blue)" stroke-width="2"/>
        <g fill="none" stroke="var(--brand-blue)" stroke-width="1.4">
          <circle cx="17" cy="17" r="8"/>
          <ellipse cx="17" cy="17" rx="3.5" ry="8"/>
          <line x1="9" y1="17" x2="25" y2="17"/>
          <line x1="10.5" y1="13" x2="23.5" y2="13"/>
          <line x1="10.5" y1="21" x2="23.5" y2="21"/>
        </g>
      </svg>
      <span class="contact-rule"></span>
      <p>dale@copperlinepipeworks.example<br>www.copperlinepipeworks.example</p>
    </div>
  </section>

</body>
</html>
```